International travel site frontpage redesign

We sell tours to Scandinavia through our website www.velmora-journeys.com. The website has become a bit old fashioned and we are in the process of making the website responsive. As you can see from the attached pictures the website will be wider with the responsive design, and our current design does not fit anymore.

Here is what we are looking for:
- A website that reflects a trustworthy and quality oriented company.
- Making the website more modern looking, but still recognisable (we want to keep the colours).
- keeping in mind that the age group of our customers are from 20-80 years old (most in their 60s).
- We want to remove the popular tours part and are instead looking to replace this with picture boxes the following subjects Scandinavia Specialist, Special Offers, Contact, Norway (or Norway Tours), Sweden (or Sweden Tours), Iceland (or Iceland Tours), Combination Tours. Possibly also Lapland, Winter, Northern Lights, Fjords and Capitals. Some of these categories can be smaller or perhaps half boxes; i.e. Winter and Northern lights in one. If we end up with four boxes per line perhaps we could add a social media box next to the three first ones.
- The above means that the left hand meny with Norway Tours, Sweden Tours etc will be redundant.
- we will add another line to the search Box (on the top): Destinations
- The top menu will have the same categories, but we need to add languages as the website will be in English and German.
- The footer must be changed
- We can take away the box to the right where it says "your window to booking the best of our world"

Reason: One of the decission makers had to go away on business last minute.

Target Market(s)

Travelling to Scandinavia is not low cost, so the website needs to appeal to those that can afford to travel to our destination.
The age group of our customers are from 20-80 years old (most in their 60s).

Industry/Entity Type

Travel

Number of Pages Required

1 page

Requirements
Should not have
• Flashy or cheap looking special offers...

```html
<!DOCTYPE html>
<html lang="en">
<head>
<meta charset="utf-8">
<title>Velmora Journeys – Search</title>
<link rel="stylesheet" href="https://fonts.googleapis.com/css2?family=Open+Sans:wght@300;400;600;700&display=swap">
<style>
  :root {
    --page-bg: #ffffff;
    --header-bg: #ffffff;
    --brand-grey: #5a5a5a;
    --brand-red: #b8232a;
    --accent-line: #d2373a;
    --icon-grey: #d4d4d4;
    --navy: #15243a;
    --navy-light: #1d2f49;
    --field-bg: #ffffff;
    --placeholder: #a9a9a9;
    --label: #ffffff;
  }
  * { box-sizing: border-box; margin: 0; padding: 0; }
  html, body {
    width: 1200px; height: 1000px; overflow: hidden;
    background: var(--page-bg);
    font-family: "Open Sans", Arial, sans-serif;
  }
  .screen {
    position: absolute; left: 344px; top: 46px;
    width: 320px; height: 568px;
    transform: scale(1.6); transform-origin: 0 0;
    overflow: hidden; background: var(--navy);
  }
  .site-header { background: var(--header-bg); height: 126px; position: relative; border-bottom: 3px solid var(--accent-line); }
  .brand {
    position: absolute; left: 0; right: 0; top: 32px;
    display: flex; align-items: center; justify-content: center; gap: 8px;
  }
  .brand-dot { width: 10px; height: 10px; border-radius: 50%; background: var(--brand-red); }
  .brand-name {
    font-size: 17px; font-weight: 400; letter-spacing: 1.5px;
    color: var(--brand-grey); text-transform: uppercase;
  }
  .toolbar { position: absolute; left: 20px; right: 20px; top: 82px; height: 24px; display: flex; align-items: center; }
  .toolbar .menu { margin-right: 30px; }
  .toolbar .lang { margin-left: auto; display: flex; align-items: center; gap: 3px; }
  .search-panel {
    padding: 14px 20px 0;
    background: linear-gradient(160deg, var(--navy-light) 0%, var(--navy) 45%);
    height: 100%;
  }
  .search-title { font-size: 35px; font-weight: 400; color: var(--label); line-height: 44px; margin-bottom: 14px; }
  .field { margin-bottom: 16px; }
  .field-label { display: block; font-size: 14px; font-weight: 600; color: var(--label); line-height: 20px; margin-bottom: 5px; }
  .field-box {
    height: 38px; border-radius: 3px; background: var(--field-bg);
    display: flex; align-items: center; padding: 0 11px;
    font-size: 14px; color: var(--placeholder);
  }
  .field-box span { flex: 1; }
</style>
</head>
<body>
  <main class="screen">
    <header class="site-header">
      <div class="brand">
        <span class="brand-dot"></span>
        <span class="brand-name">Velmora Journeys</span>
      </div>
      <nav class="toolbar">
        <svg class="menu" width="20" height="18" viewBox="0 0 20 18" aria-label="Menu">
          <rect y="1" width="20" height="3" fill="var(--icon-grey)"/>
          <rect y="7.5" width="20" height="3" fill="var(--icon-grey)"/>
          <rect y="14" width="20" height="3" fill="var(--icon-grey)"/>
        </svg>
        <svg width="22" height="22" viewBox="0 0 22 22" aria-label="Search">
          <circle cx="9" cy="9" r="6.5" fill="none" stroke="var(--brand-red)" stroke-width="3"/>
          <line x1="13.8" y1="13.8" x2="20" y2="20" stroke="var(--brand-red)" stroke-width="3.4" stroke-linecap="round"/>
        </svg>
        <div class="lang" aria-label="Language: English">
          <svg width="16" height="11" viewBox="0 0 16 11">
            <rect width="16" height="11" fill="#2b3f8a"/>
            <path d="M0 0L16 11M16 0L0 11" stroke="#fff" stroke-width="2"/>
            <path d="M0 0L16 11M16 0L0 11" stroke="#c8202f" stroke-width="0.8"/>
            <rect x="6.3" width="3.4" height="11" fill="#fff"/>
            <rect y="3.8" width="16" height="3.4" fill="#fff"/>
            <rect x="7" width="2" height="11" fill="#c8202f"/>
            <rect y="4.5" width="16" height="2" fill="#c8202f"/>
          </svg>
          <svg width="9" height="6" viewBox="0 0 9 6"><path d="M0 0H9L4.5 5Z" fill="var(--icon-grey)"/></svg>
        </div>
      </nav>
    </header>

    <section class="search-panel">
      <h1 class="search-title">Search ...</h1>
      <div class="field">
        <label class="field-label">Free Search</label>
        <div class="field-box">
          <span></span>
          <svg width="22" height="22" viewBox="0 0 22 22">
            <circle cx="9" cy="9" r="6.5" fill="none" stroke="var(--icon-grey)" stroke-width="3"/>
            <line x1="13.8" y1="13.8" x2="20" y2="20" stroke="var(--icon-grey)" stroke-width="3.4" stroke-linecap="round"/>
          </svg>
        </div>
      </div>
      <div class="field">
        <label class="field-label">Tour Type</label>
        <div class="field-box"><span>All tour types</span><svg width="10" height="6" viewBox="0 0 10 6"><path d="M0 0H10L5 6Z" fill="var(--icon-grey)"/></svg></div>
      </div>
      <div class="field">
        <label class="field-label">Tour Selection</label>
        <div class="field-box"><span>All tour selections</span><svg width="10" height="6" viewBox="0 0 10 6"><path d="M0 0H10L5 6Z" fill="var(--icon-grey)"/></svg></div>
      </div>
      <div class="field">
        <label class="field-label">Travel Period</label>
        <div class="field-box"><span>All travel periods</span><svg width="10" height="6" viewBox="0 0 10 6"><path d="M0 0H10L5 6Z" fill="var(--icon-grey)"/></svg></div>
      </div>
      <div class="field">
        <label class="field-label">Destination</label>
        <div class="field-box"><span>All destinations</span><svg width="10" height="6" viewBox="0 0 10 6"><path d="M0 0H10L5 6Z" fill="var(--icon-grey)"/></svg></div>
      </div>
    </section>
  </main>
</body>
</html>
```